New flavour! New packaging for Vortex Energy Drink!

We need a new packaging designed to show off our new grape flavored energy drink! It will require box design with matching sachets!

Established in 2018 we are a fully Australian owned and operated business that started out with 2 gamers that got sick and tired of sugary energy drinks OR expensive powder from the USA.

We are an energy drink in the esports and gaming space. Our new product is an energy drink in powder in boxes of 30 sachets (please see attached for product example)

Please see example 1 and 2 for our competitors product. We would ideally like to go a bit more minimalist than them but still have a great color pop on black backing.

Target Market(s)

Gamer's and esports athletes between the ages or 18-30

Font styles to use
Sans Serif
Other font styles liked:
• Helvetica

Colors
886aae
ffffff

Requirements
Must have
• Black base/background.
• Vibrant purple N in the Vortex Logo.
• Same or slightly different shades of purple for some text and highlights.
• Black, white and some shades of a vibrant purple (for the grape flavor)
• ingredients list (may need to be reformatted to suit)
• Please see attached for legislative requirements on the box and sachets.
Nice to have
• minimalist design but enough to be eye catching and somewhat playful
• Twitter: @VRTX_PWR
• Instagram: @VRTX_PWR
• Facebook: @VRTXPWR
Should not have
• OTHER COLORS.
• Overly complex designs.

```html
<!DOCTYPE html>
<html lang="en">
<head>
<meta charset="utf-8">
<title>Vortex Energy Drink – Grape Flavour Carton Dieline</title>
<link rel="stylesheet" href="https://fonts.googleapis.com/css2?family=Rajdhani:wght@500;600;700&display=swap">
<style>
  :root {
    --paper: #ffffff;
    --carton-black: #000000;
    --vivid-purple: #9d1ff0;
    --deep-purple: #6a12b8;
    --soft-purple: #b44cff;
    --brand-white: #ffffff;
    --fold-line: #5a5a5a;
  }
  html, body {
    margin: 0;
    padding: 0;
    width: 1200px;
    height: 1200px;
    overflow: hidden;
    background: var(--paper);
  }
  .dieline { display: block; width: 1200px; height: 1200px; }
  .carton-surface { fill: var(--carton-black); }
  .fold { stroke: var(--fold-line); stroke-width: 1.2; stroke-dasharray: 5 4; fill: none; }
  .base-band { fill: var(--vivid-purple); }
  .panel-frame { fill: none; stroke: var(--vivid-purple); stroke-width: 2; }
  .streak-line { stroke: #d9d9d9; stroke-width: 1.5; }
  .wordmark {
    font-family: "Rajdhani", sans-serif;
    font-weight: 700;
    fill: var(--brand-white);
    letter-spacing: 2px;
  }
  .product-title {
    font-family: "Rajdhani", sans-serif;
    font-weight: 700;
    font-size: 34px;
    fill: var(--brand-white);
  }
  .tagline {
    font-family: "Rajdhani", sans-serif;
    font-weight: 600;
    font-size: 14px;
    fill: var(--soft-purple);
    letter-spacing: 0.5px;
  }
  .tagline-rule { stroke: var(--brand-white); stroke-width: 1.2; }
  .flavour-badge { fill: var(--vivid-purple); }
  .flavour-label {
    font-family: "Rajdhani", sans-serif;
    font-weight: 700;
    font-size: 23px;
    fill: var(--brand-white);
    letter-spacing: 0.5px;
  }
  .ingredient-note {
    font-family: "Rajdhani", sans-serif;
    font-weight: 500;
    font-size: 13.5px;
    fill: var(--brand-white);
  }
  .ingredient-rule { stroke: var(--brand-white); stroke-width: 1; }
  .serve-count {
    font-family: "Rajdhani", sans-serif;
    font-weight: 700;
    font-size: 34px;
    fill: var(--brand-white);
  }
  .serve-ring { fill: none; stroke: var(--vivid-purple); stroke-width: 5; }
  .serve-tag { fill: var(--brand-white); }
  .serve-word {
    font-family: "Rajdhani", sans-serif;
    font-weight: 700;
    font-size: 10px;
    fill: var(--carton-black);
  }
</style>
</head>
<body>
<svg class="dieline" viewBox="0 0 1500 1500" xmlns="http://www.w3.org/2000/svg">
  <defs>
    <linearGradient id="streak-fade-right" x1="0" x2="1" y1="0" y2="0">
      <stop offset="0" stop-color="#9d1ff0" stop-opacity="0"/>
      <stop offset="0.55" stop-color="#7a18c8" stop-opacity="0.8"/>
      <stop offset="1" stop-color="#a629ff"/>
    </linearGradient>
    <linearGradient id="streak-fade-left" x1="0" x2="1" y1="0" y2="0">
      <stop offset="0" stop-color="#a629ff"/>
      <stop offset="0.5" stop-color="#7a18c8" stop-opacity="0.8"/>
      <stop offset="1" stop-color="#9d1ff0" stop-opacity="0"/>
    </linearGradient>
    <radialGradient id="grape-splash" cx="0.5" cy="0.6" r="0.6">
      <stop offset="0" stop-color="#5b2a7a"/>
      <stop offset="0.6" stop-color="#8c4aa8"/>
      <stop offset="1" stop-color="#000000"/>
    </radialGradient>

    <g id="front-panel-art">
      <rect class="panel-frame" x="372" y="648" width="285" height="648"/>
      <line class="streak-line" x1="372" y1="755" x2="610" y2="724"/>
      <polygon points="430,768 657,733 657,743 430,772" fill="url(#streak-fade-right)"/>
      <text class="wordmark" x="512" y="866" font-size="58" text-anchor="middle" textLength="236" lengthAdjust="spacingAndGlyphs">VORTEX</text>
      <polygon points="372,942 600,912 600,916 372,953" fill="url(#streak-fade-left)"/>
      <line class="streak-line" x1="480" y1="956" x2="657" y2="933"/>
      <text class="product-title" x="516" y="1018" text-anchor="middle">ENERGY DRINK</text>
      <line class="tagline-rule" x1="414" y1="1030" x2="434" y2="1030"/>
      <text class="tagline" x="516" y="1035" text-anchor="middle">FOR GAMERS, BY GAMERS</text>
      <line class="tagline-rule" x1="598" y1="1030" x2="618" y2="1030"/>
      <ellipse cx="516" cy="1098" rx="78" ry="52" fill="url(#grape-splash)" role="img" aria-label="Splash of grape juice with a cluster of purple grapes"/>
      <polygon class="flavour-badge" points="422,1142 620,1142 610,1172 414,1172"/>
      <text class="flavour-label" x="516" y="1166" text-anchor="middle">GRAPE FLAVOUR</text>
      <line class="ingredient-rule" x1="432" y1="1190" x2="600" y2="1190"/>
      <text class="ingredient-note" x="516" y="1207" text-anchor="middle">WITH GINSENG &amp; CAFFEINE</text>
      <line class="ingredient-rule" x1="432" y1="1213" x2="600" y2="1213"/>
      <circle class="serve-ring" cx="516" cy="1260" r="22"/>
      <text class="serve-count" x="516" y="1272" text-anchor="middle">30</text>
      <rect class="serve-tag" x="492" y="1276" width="48" height="12"/>
      <text class="serve-word" x="516" y="1285.5" text-anchor="middle">SERVES</text>
    </g>

    <g id="side-panel-art">
      <text class="wordmark" transform="translate(248 1182) rotate(-90)" font-size="96" textLength="436" lengthAdjust="spacingAndGlyphs">VORTEX</text>
    </g>
  </defs>

  <!-- Top closures -->
  <polygon class="carton-surface" points="107,632 107,605 148,481 348,481 348,632"/>
  <path class="carton-surface" d="M358,632 V388 H364 V360 Q364,345 380,345 H658 Q674,345 674,360 V388 H678 V632 Z"/>
  <polygon class="carton-surface" points="688,632 688,481 888,481 930,605 930,632"/>

  <!-- Body panels -->
  <rect class="carton-surface" x="107" y="632" width="1143" height="678"/>
  <polygon class="carton-surface" points="1250,632 1313,647 1313,1295 1250,1310"/>
  <rect class="base-band" x="107" y="1298" width="1143" height="12"/>
  <polygon class="base-band" points="1250,1298 1300,1298 1250,1310"/>

  <!-- Bottom closures -->
  <polygon class="carton-surface" points="107,1310 358,1310 358,1313 166,1438 166,1480 107,1480"/>
  <polygon class="carton-surface" points="358,1310 678,1310 678,1475 620,1475 620,1440 400,1440 400,1475 358,1475"/>
  <polygon class="carton-surface" points="678,1310 930,1310 930,1480 872,1480 872,1440 678,1313"/>
  <polygon class="carton-surface" points="930,1310 1250,1310 1190,1440 990,1440"/>
  <rect class="carton-surface" x="990" y="1435" width="200" height="40" rx="8"/>

  <!-- Fold lines -->
  <line class="fold" x1="107" y1="632" x2="1250" y2="632"/>
  <line class="fold" x1="107" y1="1310" x2="1250" y2="1310"/>
  <line class="fold" x1="364" y1="388" x2="674" y2="388"/>
  <line class="fold" x1="358" y1="632" x2="358" y2="1310"/>
  <line class="fold" x1="678" y1="632" x2="678" y2="1310"/>
  <line class="fold" x1="930" y1="632" x2="930" y2="1310"/>
  <line class="fold" x1="1250" y1="632" x2="1250" y2="1310"/>

  <!-- Printed artwork -->
  <use href="#side-panel-art"/>
  <use href="#front-panel-art"/>
  <use href="#side-panel-art" transform="translate(578 0)"/>
  <use href="#front-panel-art" transform="translate(576 0)"/>
</svg>
</body>
</html>
```